bramblewood ridge livestock company website

we would like a home page, an about us page, a page for sires, a page for dams, A sale page where we can list progreny for sale and a contact us. on the about us page we would like there to be a family picture. on the sires page we would like to have a picture of each sire, a description beside them and a link to their online profile at prairie hereford. on the dam page we would like to have a picture of each dam, aswell as a description beside them aswell as a link to the prairie hereford site. would like the website to very mobile phone friendly as expecting most traffic to be on phone. we would like the website to look and feel very mich like a farm, rustic, barbed wire and other farm feels. we would also like a frozen genetics pages where we can include pictures and descriptions of the sires and dams aswell as a price for embryos and semen. we need to website to be easy to maintain so we can update pictures and information as it changes, we would like there to be a feature so that people can sign up to be on our mailing list by giving us their mailing addess and email and full name
aswell as an area where they can send us a message to contact us.

leaving for work for 3 weeks in the canadian arctic will have limited ability to use the internet

Target Market(s)

other ranchers, farmers, cattlemen,

Industry/Entity Type

farming, agriculture, cattle

Coding

Coded - Design and coding required

Requirements
Must have
• about page, contact page, sires page, dams page, SALE page.
Nice to have
• country/farm vibe, barbed wire, wood,

```html
<!DOCTYPE html>
<html lang="en">
<head>
<meta charset="utf-8">
<title>Bramblewood Ridge Livestock Company — Premium Angus Genetics</title>
<link href="https://fonts.googleapis.com/css2?family=Bebas+Neue&family=Poppins:wght@400;500;600&display=swap" rel="stylesheet">
<style>
:root{
  --ink:#1f1f1f;
  --text:#3a3a3a;
  --white:#ffffff;
  --charcoal:#3f3f3f;
  --stone:#ebebeb;
  --blush:#e6dcdc;
  --slate:#cfcfcf;
  --line:#9a9a9a;
  --button-dark:#6b6868;
  --gold:#e0a23a;
}
*{box-sizing:border-box;margin:0;padding:0}
html,body{width:1200px;height:4332px;overflow:hidden}
body{position:relative;background:var(--white);font-family:"Poppins",sans-serif;color:var(--text)}
.section{position:absolute;left:0;width:1200px}
.abs{position:absolute}
.display{font-family:"Bebas Neue",sans-serif;color:var(--ink);font-weight:400;line-height:1}
.body-copy{font-size:10.5px;line-height:1.6}
.pill{position:absolute;display:flex;align-items:center;justify-content:center;border-radius:20px;font-size:9.5px;font-weight:600;text-transform:uppercase;background:var(--white);color:var(--ink)}
.pill.ghost{background:transparent;border:1.5px solid var(--white);color:var(--white)}
.photo{position:absolute}

/* top bar */
.topbar{top:0;height:24px;background:var(--white);text-align:center;font-size:9px;font-weight:600;letter-spacing:14px;line-height:24px;color:var(--ink)}

/* hero */
.hero{top:24px;height:742px;background:linear-gradient(180deg,#3d3f30 0%,#4e4b35 20%,#7a6a3e 32%,#b7823a 45%,#cf9444 62%,#a8702d 82%,#7e5220 100%)}
.brand{position:absolute;font-family:"Poppins",sans-serif;font-weight:600;text-transform:uppercase;line-height:1.15;letter-spacing:.5px}
.hero .brand{left:128px;top:14px;width:110px;font-size:10px;color:var(--white);text-align:center}
.nav{position:absolute;left:418px;top:30px;display:flex;gap:22px;font-size:9.5px;font-weight:600;color:var(--white);text-transform:uppercase}
.hero-title{position:absolute;top:124px;width:1200px;text-align:center;font-size:72px;color:var(--white);line-height:.93}
.hero-sub{position:absolute;top:264px;width:1200px;text-align:center;font-size:11.5px;font-weight:500;color:var(--white);line-height:1.7}

/* focus */
.focus-dark{top:766px;height:384px;background:var(--charcoal)}
.focus-light{top:1150px;height:524px;background:var(--stone)}
.center-head{position:absolute;width:1200px;text-align:center}
.card{position:absolute;top:970px;height:331px;width:276px;background:var(--white);border-radius:8px;box-shadow:0 6px 18px rgba(0,0,0,.12);padding:7px}
.card .photo{position:relative;height:173px;border-radius:6px 6px 0 0}
.card h3{font-family:"Bebas Neue",sans-serif;font-weight:400;font-size:17px;color:var(--ink);margin:44px 0 0 18px}
.card p{font-size:9.5px;line-height:1.6;margin:10px 18px 0;color:var(--text)}

/* offer */
.offer{top:2010px;height:518px;background:var(--blush)}
.offer-item{position:absolute;top:190px;width:260px;text-align:center}
.offer-item .photo{position:relative;margin:0 auto;width:158px;height:158px;border-radius:50%;border:2px solid var(--ink)}
.offer-item h3{font-family:"Bebas Neue",sans-serif;font-weight:400;font-size:17px;color:var(--ink);margin-top:17px}
.offer-item p{font-size:9.5px;line-height:1.6;margin-top:8px}

/* genetics */
.genetics{top:2528px;height:739px;background:var(--slate)}

/* testimonials */
.testimonials{top:3267px;height:501px;background:linear-gradient(180deg,#ffffff 0%,#f6f2ea 35%,#e9dcc4 60%,#c9c07f 85%,#a7a45a 100%)}

/* contact */
.contact-card{position:absolute;left:360px;top:3580px;width:470px;height:361px;background:var(--white);border-radius:6px;box-shadow:0 6px 0 var(--button-dark),0 8px 20px rgba(0,0,0,.1);padding:0 38px}
.field{position:absolute;font-size:6.5px;letter-spacing:1px;text-transform:uppercase;color:var(--text);border-bottom:1px solid var(--line);height:28px;padding-top:2px}

/* footer */
.footer-head{font-family:"Bebas Neue",sans-serif;font-size:20px;color:var(--ink);position:absolute}
.footer-list{position:absolute;font-size:9.5px;line-height:25px;list-style:none;color:var(--text)}
.social{position:absolute;top:4140px;width:20px;height:20px;border-radius:50%;border:1px solid var(--ink)}
</style>
</head>
<body>

<div class="section topbar">FAMILY ANGUS FARM</div>

<header class="section hero" role="img" aria-label="Angus cattle grazing in a golden pasture at sunset, dark pine trees behind">
  <div class="brand">Bramblewood Ridge Livestock Company</div>
  <nav class="nav"><span>Home</span><span>About Us</span><span>Sires KA</span><span>Dams KA</span><span>Sale</span><span>Contact Us</span></nav>
  <div class="pill ghost" style="left:857px;top:18px;width:104px;height:34px">Login</div>
  <div class="pill" style="left:966px;top:18px;width:102px;height:34px">Sign Up</div>
  <h1 class="display hero-title">Premium Angus Genetics<br>Raised With Pride</h1>
  <p class="hero-sub">Quality-focused breeding, proven bloodlines, and a commitment to strong, reliable cattle for today's<br>ranchers and tomorrow's herds.</p>
  <div class="pill" style="left:485px;top:320px;width:108px;height:34px">View Our Sires</div>
  <div class="pill ghost" style="left:600px;top:320px;width:115px;height:34px">Cattle For Sale</div>
</header>

<section class="section focus-dark">
  <h2 class="display center-head" style="top:76px;font-size:34px;color:var(--white)">Focused On What Matters Most</h2>
  <p class="center-head body-copy" style="top:116px;color:#e6e6e6;font-size:9.5px">We prioritize the qualities that truly make a difference in our breeding program. Our herd is built on proven bloodlines,<br>functional cattle raised under real ranch conditions, and a commitment to honest, reliable service. Every animal re-<br>flects our dedication to producing strong, healthy, and productive Angus cattle for ranchers and breeders alike.</p>
</section>
<section class="section focus-light"></section>

<article class="card" style="left:171px">
  <div class="photo" role="img" aria-label="Red Angus cow resting in green grass" style="background:linear-gradient(160deg,#7f9a4a,#9a6a3a 55%,#6d8a3e)"></div>
  <h3>Proven Bloodlines</h3>
  <p>Carefully selected sires and dams backed by strong performance and pedigree data.</p>
</article>
<article class="card" style="left:462px">
  <div class="photo" role="img" aria-label="Ranch couple standing with cattle in a pasture" style="background:linear-gradient(160deg,#6e7a52,#5a4536 50%,#8a9a5c)"></div>
  <h3>Functional, Real-World Cattle</h3>
  <p>Raised in practical ranch conditions to ensure durability, fertility, and longevity.</p>
</article>
<article class="card" style="left:753px">
  <div class="photo" role="img" aria-label="Rancher standing in a field with his herd" style="background:linear-gradient(160deg,#8aa7c4,#6f8f55 45%,#4d5a44)"></div>
  <h3>Honest, Straightforward Service</h3>
  <p>We believe in transparency, long-term relation-ships, and helping fellow cattlemen succeed.</p>
</article>

<h2 class="display abs" style="left:166px;top:1394px;font-size:36px;line-height:1.03">Built On Family, Tradition, And<br>Strong Genetics</h2>
<p class="abs body-copy" style="left:167px;top:1474px;width:420px;font-size:9.5px">We are a family-run cattle operation dedicated to producing high-quality Angus genetics for commercial and purebred breeders.<br>Our program focuses on structure, temperament, performance, and maternal strength — ensuring cattle that work in real ranch conditions.<br><br>Every animal we raise reflects our commitment to honest breeding, careful selec-tion, and long-term herd improvement.</p>
<div class="photo" role="img" aria-label="Red Angus bull standing in profile" style="left:628px;top:1360px;width:412px;height:240px;background:radial-gradient(ellipse 48% 38% at 50% 45%,#7a3e1e 0%,#6a3418 70%,rgba(106,52,24,0) 72%)"></div>

<section class="section" style="top:1674px;height:336px;background:linear-gradient(90deg,#3b2d25 0%,#4a3a30 45%,#5d5a57 75%,#2e2a27 100%)" role="img" aria-label="Cattle feeding in a barn beside a steel milk can">
  <h2 class="display abs" style="left:166px;top:108px;font-size:32px;color:var(--white)">Meet Our Herd Sires</h2>
  <p class="abs body-copy" style="left:165px;top:152px;color:var(--white);font-size:9.5px">Our herd sires represent the foundation of our breeding program — selected for<br>performance, structure, and maternal influence.</p>
  <div class="pill" style="left:166px;top:190px;width:108px;height:34px">View All Sires</div>
</section>

<section class="section offer">
  <h2 class="display center-head" style="top:66px;font-size:34px">What We Offer</h2>
  <p class="center-head body-copy" style="top:107px;font-size:9.5px">We provide high-quality Angus genetics through carefully selected sires and dams, functional cattle raised for real ranch<br>conditions, honest and transparent service for our clients, and access to frozen genetics including embryos and semen from<br>elite animals. Our goal is to support ranchers and breeders with strong, reliable, and productive cattle.</p>
  <div class="offer-item" style="left:169px">
    <div class="photo" role="img" aria-label="Rancher checking a cow inside a barn" style="background:linear-gradient(160deg,#8a8580,#3a3430 55%,#6e665e)"></div>
    <h3>Proven Bloodlines</h3>
    <p>Carefully selected sires and dams with strong pedigrees and performance records, ensuring quality genetics for your herd.</p>
  </div>
  <div class="offer-item" style="left:467px">
    <div class="photo" role="img" aria-label="Rancher tending black cattle in a green pasture" style="background:linear-gradient(160deg,#6f8e45,#2c2a24 50%,#7c9a50)"></div>
    <h3>Functional, Real-World Cattle</h3>
    <p>Cattle raised under practical ranch conditions for strength, fertility, and longevity, ready to perform in real-world environments.</p>
  </div>
  <div class="offer-item" style="left:769px">
    <div class="photo" role="img" aria-label="Rancher with a calf in a corral" style="background:linear-gradient(160deg,#b7a58c,#8a5a3a 55%,#c4a07a)"></div>
    <h3>Honest, Straightforward Service</h3>
    <p>We value transparency, long-term relation-ships, providing guidance and support to help fellow ranchers succeed.</p>
  </div>
</section>

<section class="section genetics">
  <div class="photo" role="img" aria-label="Family portrait in front of a wooden barn" style="left:160px;top:75px;width:440px;height:293px;border-radius:4px;background:linear-gradient(160deg,#6b4a32,#4a3222 50%,#7c5a3e)"></div>
  <h2 class="display abs" style="left:640px;top:127px;font-size:34px">Quality Cattle Available</h2>
  <p class="abs body-copy" style="left:643px;top:173px;width:310px;font-size:9.5px">We offer select progeny throughout the year, including bulls, heifers, and replacement females bred for performance and longevity.<br><br>Whether you're building a herd or strengthening genetics, we're here to help you find the right fit.</p>
  <div class="pill" style="left:640px;top:283px;width:140px;height:34px">View Sale Listings</div>

  <h2 class="display abs" style="left:168px;top:432px;font-size:34px">Frozen Genetics Available</h2>
  <p class="abs body-copy" style="left:167px;top:480px;width:310px;font-size:9.5px">Embryos and semen from our proven sires and elite donor dams are available in limited quantities.<br><br>This gives breeders access to top-tier genetics while accel-erating herd improvement.</p>
  <div class="pill" style="left:163px;top:590px;width:177px;height:34px">Explore Frozen Genetics</div>
  <div class="photo" role="img" aria-label="Couple standing with a red Angus cow in a green pasture" style="left:602px;top:370px;width:440px;height:292px;border-radius:4px;background:linear-gradient(160deg,#8aa35a,#8b5530 50%,#6e8a3e)"></div>
</section>

<section class="section testimonials" role="img" aria-label="Misty morning field with a rancher in a hat">
  <h2 class="display abs" style="left:131px;top:100px;font-size:32px">Testimonials</h2>
  <h3 class="display abs" style="left:131px;top:172px;font-size:15px">Dale M., Wyoming Rancher</h3>
  <p class="abs body-copy" style="left:131px;top:198px;width:500px;font-size:9.5px">The quality of their Angus cattle is outstanding. Every bull and heifer we purchased has performed beyond expectations. Working with this farm has been a pleasure. Honest, knowledgeable, and always helpful in guiding us with our herd decisions. Their frozen genetics program allowed us to access elite bloodlines we wouldn't have been able to otherwise. Highly recommended</p>
  <svg class="abs" style="left:131px;top:280px" width="64" height="12" viewBox="0 0 64 12" aria-hidden="true">
    <g fill="var(--gold)">
      <polygon points="6,0 7.6,4 12,4.3 8.6,7 9.7,11.5 6,9 2.3,11.5 3.4,7 0,4.3 4.4,4"/>
      <polygon transform="translate(13 0)" points="6,0 7.6,4 12,4.3 8.6,7 9.7,11.5 6,9 2.3,11.5 3.4,7 0,4.3 4.4,4"/>
      <polygon transform="translate(26 0)" points="6,0 7.6,4 12,4.3 8.6,7 9.7,11.5 6,9 2.3,11.5 3.4,7 0,4.3 4.4,4"/>
      <polygon transform="translate(39 0)" points="6,0 7.6,4 12,4.3 8.6,7 9.7,11.5 6,9 2.3,11.5 3.4,7 0,4.3 4.4,4"/>
      <polygon transform="translate(52 0)" points="6,0 7.6,4 12,4.3 8.6,7 9.7,11.5 6,9 2.3,11.5 3.4,7 0,4.3 4.4,4"/>
    </g>
  </svg>
  <svg class="abs" style="left:131px;top:308px" width="44" height="12" viewBox="0 0 44 12" aria-hidden="true">
    <circle cx="3" cy="6" r="2.2" fill="#bbb"/>
    <circle cx="14" cy="6" r="4.5" fill="none" stroke="#555"/><circle cx="14" cy="6" r="2.2" fill="#555"/>
    <circle cx="25" cy="6" r="2.2" fill="#bbb"/><circle cx="36" cy="6" r="2.2" fill="#bbb"/>
  </svg>
</section>

<section class="contact-card">
  <h2 class="display" style="text-align:center;margin-top:50px;font-size:34px;line-height:1">Get In Touch,<br>We're Here To Help</h2>
  <div class="field" style="left:38px;top:130px;width:188px">Name*</div>
  <div class="field" style="left:244px;top:130px;width:188px">Email*</div>
  <div class="field" style="left:38px;top:180px;width:188px">Phone*</div>
  <div class="field" style="left:244px;top:180px;width:188px">Subject*</div>
  <div class="field" style="left:38px;top:227px;width:394px;height:34px">Message*</div>
  <div class="pill" style="left:174px;top:290px;width:134px;height:33px;background:var(--button-dark);color:var(--white)">Submit Request</div>
</section>
<svg class="abs" style="left:573px;top:3560px" width="40" height="40" viewBox="0 0 40 40" aria-hidden="true">
  <circle cx="20" cy="20" r="19" fill="var(--button-dark)" stroke="var(--white)" stroke-width="2"/>
  <rect x="13" y="15" width="14" height="10" rx="1" fill="var(--white)"/>
  <path d="M13 15 L20 21 L27 15" fill="none" stroke="var(--button-dark)" stroke-width="1.2"/>
</svg>

<footer>
  <div class="brand" style="left:134px;top:4080px;width:180px;font-size:15px;color:var(--ink);text-align:center">Bramblewood Ridge<br>Livestock Company</div>

  <h4 class="footer-head" style="left:403px;top:4018px">Useful Links</h4>
  <ul class="footer-list" style="left:403px;top:4044px"><li>Home</li><li>About Us</li><li>Sires KA</li><li>Dams KA</li><li>Sale</li><li>Contact Us</li></ul>

  <h4 class="footer-head" style="left:575px;top:4018px">Contact Us</h4>
  <div class="abs" style="left:576px;top:4050px;font-size:8.5px;line-height:1.55;color:var(--text)">
    <b style="font-weight:600;color:var(--ink)">PHONE:</b><br>(555) 014-2760<br><br>
    <b style="font-weight:600;color:var(--ink)">EMAIL:</b><br>hello@bramblewoodridge.com<br><br>
    <b style="font-weight:600;color:var(--ink)">ADDRESS:</b><br>Reference site about Lorem Ipsum,
  </div>

  <h4 class="footer-head" style="left:795px;top:4018px">Newsletter</h4>
  <p class="abs" style="left:795px;top:4050px;font-size:9.5px">Get Latest Updates And Offers</p>
  <div class="abs" style="left:792px;top:4077px;width:275px;height:44px;border-radius:22px;background:#ececec;overflow:hidden">
    <span class="abs" style="left:18px;top:15px;font-size:9px;color:var(--text)">Enter Your email Address</span>
    <div class="abs" style="right:0;top:0;width:64px;height:44px;background:var(--button-dark)"></div>
    <svg class="abs" style="right:22px;top:13px" width="20" height="18" viewBox="0 0 20 18" aria-hidden="true"><path d="M1 8 L19 1 L13 17 L9 10 Z" fill="var(--white)"/></svg>
  </div>
  <div class="social" style="left:810px"></div>
  <div class="social" style="left:842px"></div>
  <div class="social" style="left:874px;background:var(--ink)"></div>
  <div class="social" style="left:906px"></div>
  <div class="social" style="left:938px"></div>

  <div class="abs" style="left:131px;top:4266px;width:938px;height:1px;background:#d6d6d6"></div>
  <p class="abs" style="left:0;top:4289px;width:1200px;text-align:center;font-size:9px">© 2026 All Rights Reserved</p>
  <svg class="abs" style="left:1126px;top:4250px" width="34" height="30" viewBox="0 0 34 30" aria-hidden="true">
    <path d="M4 4 h22 a4 4 0 0 1 4 4 v10 a4 4 0 0 1 -4 4 h-12 l-7 6 v-6 h-3 a4 4 0 0 1 -4 -4 v-10 a4 4 0 0 1 4 -4z" fill="#4a4a4a"/>
    <circle cx="10" cy="13" r="1.6" fill="#fff"/><circle cx="15" cy="13" r="1.6" fill="#fff"/><circle cx="20" cy="13" r="1.6" fill="#fff"/>
  </svg>
</footer>

</body>
</html>
```